Customizable Gift Note Card Design

I need a gift note card designed for my Healthy Snacks Care Package company. I need to be able to customize each card with the customer's gift message to the recipient and print to a standard printer.

The card should be single-sided 5 x 7, include our logo, keep colors and graphics simple since they will be printed for each individual order on a standard printer. I would like the following quote to be included in a small and subtle way: "Food is symbolic of love when words are inadequate." —Bertram K. Osslund. Our website thebrightpantrybites.example should also be included.

I have included pictures of our product packaging for reference.

Target Market(s)

Gift recipients: Students, people recovering from illness, housewarming, thank you gifts...etc.

Industry/Entity Type

It Company

Colors

Designer to choose colors to be used in the design.

Requirements
Must have
• We are looking for a simple, cute and elegant gift card that reflects our branding. Must be customizable and printable on a standard printer.
• Must be single-sided 5x7.

```html
<!DOCTYPE html>
<html lang="en">
<head>
<meta charset="utf-8">
<title>The Bright Pantry – Gift Note Card</title>
<link rel="stylesheet" href="https://fonts.googleapis.com/css2?family=Nunito+Sans:wght@400;700;800&display=swap">
<style>
  :root {
    --paper: #ffffff;
    --ink: #1d1a18;
    --brand-red: #b3151b;
    --ribbon-red: #9b1a22;
    --kraft-back: #b8946a;
    --kraft-front: #caa77d;
    --kraft-front-light: #d2b088;
  }
  * { margin: 0; padding: 0; box-sizing: border-box; }
  html, body {
    width: 857px;
    height: 1200px;
    overflow: hidden;
    background: var(--paper);
  }
  .card {
    position: relative;
    width: 857px;
    height: 1200px;
    background: var(--paper);
    font-family: "Nunito Sans", Arial, sans-serif;
    overflow: hidden;
  }
  .brand {
    position: absolute;
    top: 52px;
    left: 0;
    width: 100%;
    display: flex;
    justify-content: center;
    align-items: center;
    gap: 12px;
  }
  .brand-dot {
    width: 16px;
    height: 16px;
    border-radius: 50%;
    background: var(--ink);
  }
  .brand-name {
    font-size: 30px;
    font-weight: 700;
    color: var(--ink);
    letter-spacing: 0.5px;
  }
  .message-area {
    position: absolute;
    top: 140px;
    left: 60px;
    right: 60px;
    height: 560px;
  }
  .kraft {
    position: absolute;
    inset: 0;
    width: 857px;
    height: 1200px;
  }
  .quote {
    position: absolute;
    top: 985px;
    left: 50px;
    width: 806px;
    text-align: center;
    color: var(--brand-red);
  }
  .quote-text {
    font-size: 35px;
    font-weight: 800;
    line-height: 42px;
  }
  .quote-author {
    font-size: 19px;
    font-weight: 400;
    margin-top: 2px;
  }
  .web-ribbon {
    position: absolute;
    left: 0;
    top: 1131px;
    width: 356px;
    height: 42px;
  }
  .web-address {
    position: absolute;
    left: 36px;
    top: 1131px;
    height: 42px;
    line-height: 42px;
    font-size: 17px;
    color: #ffffff;
    letter-spacing: 0.3px;
  }
</style>
</head>
<body>
  <main class="card">
    <header class="brand">
      <span class="brand-dot"></span>
      <span class="brand-name">The Bright Pantry</span>
    </header>

    <section class="message-area" aria-label="Gift message space"></section>

    <svg class="kraft" viewBox="0 0 857 1200" role="img" aria-label="Folded kraft paper panels">
      <defs>
        <linearGradient id="kraftFront" x1="0" y1="0" x2="1" y2="1">
          <stop offset="0" stop-color="var(--kraft-front-light)"/>
          <stop offset="1" stop-color="var(--kraft-front)"/>
        </linearGradient>
      </defs>
      <polygon points="0,725 432,874 0,1010" fill="var(--kraft-back)"/>
      <polygon points="857,732 857,1200 0,1200 0,1008" fill="url(#kraftFront)"/>
    </svg>

    <blockquote class="quote">
      <p class="quote-text">"Food is symbolic of love<br>when words are inadequate."</p>
      <p class="quote-author">–Bertram K. Osslund</p>
    </blockquote>

    <svg class="web-ribbon" viewBox="0 0 356 42" aria-hidden="true">
      <polygon points="0,0 356,0 334,21 356,42 0,42" fill="var(--ribbon-red)"/>
    </svg>
    <p class="web-address">www.thebrightpantrybites.example/</p>
  </main>
</body>
</html>
```